Family owned plumbing contractor needs eye catching business card design

Business cards that are unique, eye catching, and provide customers with general company information, such as name, address, phone number, website, employee name/title, cell phone #, & email address. We are transitioning to a new logo that utilizes a more retro feel, so we are interested in seeing some cool old school designs in the mix. We are liking the dark background on some of the samples on this website. If that is workable with our artwork, we would like to see that incorporated into the design.
Contact Information for Business Card
Copperline Pipeworks, Inc.
www.copperlinepipeworks.example
(555) 392-7068 phone
Nevada License #64205
California License #5810473
Dale Wrennick, President
(555) 618-9032 cell
dale@copperlinepipeworks.example
Residential * Commercial * Service
Requirements
Must have
- The business card details listed above & logo provided.
Nice to have
- I made some notes about color options in the description.

```html
<!DOCTYPE html>
<html lang="en">
<head>
<meta charset="utf-8">
<title>Copperline Pipeworks business cards</title>
<link href="https://fonts.googleapis.com/css2?family=Lato:wght@400;700&display=swap" rel="stylesheet">
<style>
  :root {
    --backdrop: #8ecbbf;
    --teal: #7ec8bb;
    --teal-text: #74c2b2;
    --slate: #55708d;
    --ink: #6a6d72;
    --rule: #8a8c90;
    --ghost: #eceef1;
    --white: #ffffff;
  }
  * { box-sizing: border-box; margin: 0; padding: 0; }
  html, body {
    width: 1200px; height: 895px; overflow: hidden;
    background: var(--backdrop);
    font-family: "Lato", sans-serif;
  }
  .sheet {
    position: relative; width: 1200px; height: 895px;
    display: flex; align-items: center; justify-content: center; gap: 40px;
  }
  .card {
    position: relative; width: 540px; height: 308px; overflow: hidden;
    box-shadow: 0 6px 18px rgba(40, 80, 75, 0.25);
  }
  /* Front */
  .card-front {
    background: var(--teal);
    display: flex; align-items: center; justify-content: center;
  }
  .front-mark {
    display: flex; align-items: center; gap: 14px;
  }
  .mark-dot {
    width: 34px; height: 34px; border-radius: 50%;
    background: var(--slate); flex: none;
  }
  .front-name {
    font-size: 30px; font-weight: 700; color: var(--white);
    line-height: 1.15; max-width: 330px;
  }
  /* Back */
  .card-back { background: var(--white); }
  .ghost-art {
    position: absolute; left: 0; top: 36px;
    width: 130px; height: 130px; border-radius: 8px;
    background: var(--ghost);
  }
  .back-mark {
    position: absolute; right: 28px; top: 28px;
    display: flex; align-items: center; gap: 10px;
  }
  .back-mark .mark-dot { width: 22px; height: 22px; }
  .back-name {
    font-size: 17px; font-weight: 700; color: var(--slate);
    line-height: 1.15; max-width: 150px;
  }
  .holder {
    position: absolute; left: 30px; top: 148px; right: 28px;
    display: flex; align-items: flex-end; gap: 10px;
  }
  .holder-name {
    font-size: 31px; font-weight: 400; color: var(--teal-text);
    white-space: nowrap; line-height: 1;
  }
  .holder-rule {
    flex: 1; height: 1px; background: var(--rule); margin-bottom: 6px;
  }
  .holder-title {
    position: absolute; left: 32px; top: 184px;
    font-size: 14px; color: var(--ink); letter-spacing: 0.3px;
  }
  .contacts {
    position: absolute; left: 30px; top: 208px;
    list-style: none; font-size: 13px; color: var(--ink);
  }
  .contacts li {
    display: flex; align-items: center; gap: 9px; height: 21px;
  }
  .contacts svg { width: 13px; height: 13px; fill: var(--slate); flex: none; }
  .company-info {
    position: absolute; right: 28px; top: 214px;
    text-align: right; font-size: 12.5px; color: var(--ink); line-height: 1.6;
  }
</style>
</head>
<body>
<main class="sheet">

  <section class="card card-front" aria-label="Card front">
    <div class="front-mark">
      <span class="mark-dot"></span>
      <span class="front-name">Copperline Pipeworks, Inc.</span>
    </div>
  </section>

  <section class="card card-back" aria-label="Card back">
    <div class="ghost-art" role="img" aria-label="Faint pipe wrench decoration"></div>

    <div class="back-mark">
      <span class="mark-dot"></span>
      <span class="back-name">Copperline Pipeworks, Inc.</span>
    </div>

    <div class="holder">
      <span class="holder-name">Dale Wrennick</span>
      <span class="holder-rule"></span>
    </div>
    <p class="holder-title">President</p>

    <ul class="contacts">
      <li>
        <svg viewBox="0 0 16 16" aria-hidden="true"><path d="M3.6 1.2l2.3 2.6-1.3 1.8c.9 2 2.6 3.7 4.6 4.6l1.8-1.3 2.6 2.3-1.3 2.3C7.6 15.2 .8 8.4 1.3 2.5z"/></svg>
        <span>(555) 392-7068</span>
      </li>
      <li>
        <svg viewBox="0 0 16 16" aria-hidden="true"><path d="M4 1h8v14H4zM5.3 2.6v9.4h5.4V2.6zM7.2 13h1.6v1H7.2z" fill-rule="evenodd"/></svg>
        <span>(555) 618-9032</span>
      </li>
      <li>
        <svg viewBox="0 0 16 16" aria-hidden="true"><path d="M1 3.5h14v9H1zM1.8 4.3L8 9l6.2-4.7v1.2L8 10.2 1.8 5.5z"/></svg>
        <span>dale@copperlinepipeworks.example</span>
      </li>
      <li>
        <svg viewBox="0 0 16 16" aria-hidden="true"><path d="M8 1a7 7 0 100 14A7 7 0 008 1zm-1 1.9C5.6 4.6 5.1 6.2 5 7.5H2.6A5.5 5.5 0 017 2.9zm2 0a5.5 5.5 0 014.4 4.6H11c-.1-1.3-.6-2.9-2-4.6zM6.5 7.5c.1-1.4.6-2.8 1.5-4 .9 1.2 1.4 2.6 1.5 4zm-3.9 1H5c.1 1.3.6 2.9 2 4.6a5.5 5.5 0 01-4.4-4.6zm3.9 0h3c-.1 1.4-.6 2.8-1.5 4-.9-1.2-1.4-2.6-1.5-4zm4.5 0h2.4A5.5 5.5 0 019 13.1c1.4-1.7 1.9-3.3 2-4.6z"/></svg>
        <span>www.copperlinepipeworks.example</span>
      </li>
    </ul>

    <div class="company-info">
      <p>Copperline Pipeworks, Inc.</p>
      <p>Nevada License #64205</p>
      <p>California License #5810473</p>
    </div>
  </section>

</main>
</body>
</html>
```